Barrel Bay Runner mobile app; beer delivery service

We are looking for a design of our app - "Barrel Bay Runner". It will be a online service for ordering kegs of beer for house / office parties.

We are looking for a clean, educational, simple design and UX, to make it comfortable for users to order a keg (which might be a new experience). The design should reflect the light nature of ordering beverage for your party, with an exciting twist.

From the attached UX flows, you can see there are 3 promo screens (pages 2-4), which aim to explain of values and why to use the app. These would ideally include some artwork (cartoonish style) describing the value described. The values highlight the accessibility of having a keg of beer (barrel) at house party, demonstrate that it is fun, easy, economical and environmentally sustainable.

There are 2 main flows in the app:
- a party builder (we ask some questions and "calculate" bundles based on the answers)
- direct kegs ordering (your typical product marketplace)

Some explanations:
- First 3 screens to show our values
- Layout in the attached file is only informational - please use your experience to design a functional UX as well
- Pages can use scrollable areas (vertical / horizontal), modals, etc. We will use FlintKit so you can use those components in your design.
- Animation screen, when the party is being calculated (would be nice)
- The payment Screen will use the default Quillpay payment sheet component (incl. Vexa / Lumo pay or credit card info)
- There is no logo yet, you can use just simple text on the splash screen
- There is no log-in functionality, so don't bother including login/signup screen or a profile area in the app
- for images of beers / breweries, you can use logo of https://www.tallowmerebrewing.co.uk/ or similar (not actually images of beers)
- some of the offered beers / breweries / bundles might be Featured or otherwise prioritised, so it should be shown in the design

Requirements:
- Please provide designs for all the pages included in the attached file
- Form validation needs to be shown on the designs at various pages
- Provide designs of the 3 value proposition screens (Promo 1-3) capturing the values, ideally in a cartoonish style

Target Market(s)

Households

Industry/Entity Type

Food and beverage, delivery

Font styles to use
Sans Serif

Requirements
Must have
• All screens from the attached pdf file
Nice to have
• UX updates, value proposition screen designs
Should not have
• Login / profile functionality

```html
<!DOCTYPE html>
<html lang="en">
<head>
<meta charset="utf-8">
<title>Barrel Bay Runner – UI Screens</title>
<link href="https://fonts.googleapis.com/css2?family=Archivo+Black&family=Montserrat:wght@400;500;600;700&display=swap" rel="stylesheet">
<style>
:root{
  --canvas:#e6e6e6;
  --yellow:#f7b500;
  --yellow-soft:#fde7a6;
  --brown:#4a2414;
  --ink:#3b2216;
  --grey-text:#7a6a60;
  --field:#f1f1f1;
  --white:#ffffff;
  --island:#1b1b1b;
  --blue:#2f8fe0;
  --orange:#e0751c;
  --teal:#1bb7c9;
  --green:#2ec45a;
}
*{box-sizing:border-box;margin:0;padding:0}
html,body{width:1012px;height:1200px;overflow:hidden}
body{background:var(--canvas);font-family:"Montserrat",sans-serif;color:var(--ink);position:relative}
.heading{position:absolute;left:0;right:0;text-align:center}
.heading h1{position:absolute;left:0;right:0;top:66px;font-family:"Archivo Black",sans-serif;font-size:52px;letter-spacing:-1px;color:var(--brown);line-height:1}
.heading p{position:absolute;left:0;right:0;top:126px;font-size:38px;font-weight:500;color:#a6a6a6;letter-spacing:1px;line-height:1}
.screen{position:absolute;width:195px;height:424px;border-radius:24px;overflow:hidden;background:var(--white)}
.screen.promo{background:var(--yellow)}
.row1{top:242px}.row2{top:701px}
.c1{left:63px}.c2{left:293px}.c3{left:524px}.c4{left:754px}
.time{position:absolute;left:26px;top:10px;font-size:9px;font-weight:600;color:var(--ink)}
.island{position:absolute;left:66px;top:6px;width:63px;height:17px;border-radius:9px;background:var(--island)}
.status-icons{position:absolute;left:138px;top:12px}
.art{position:absolute;border-radius:14px}
.promo-title{position:absolute;left:12px;right:10px;font-family:"Archivo Black",sans-serif;font-size:10.5px;line-height:13px;color:var(--brown)}
.promo-title.single-line{right:4px;font-size:9.6px;letter-spacing:-0.1px;white-space:nowrap}
.promo-body{position:absolute;left:12px;right:10px;font-size:7px;line-height:11px;color:var(--brown)}
.promo-body p{margin-bottom:11px}
.promo-body b{font-weight:700}
.dots{position:absolute;left:12px;top:359px;width:36px;height:11px;border-radius:6px;background:rgba(255,255,255,.3);display:flex;gap:5px;align-items:center;justify-content:center}
.dots i{width:3.5px;height:3.5px;border-radius:50%;background:rgba(255,255,255,.55)}
.dots i.on{background:var(--white)}
.nav-link{position:absolute;top:390px;font-size:9.5px;font-weight:700;color:var(--brown)}
.nav-link.back{left:12px}.nav-link.next{right:12px}
.brand-mark{position:absolute;left:0;right:0;top:172px;text-align:center;font-family:"Archivo Black",sans-serif;font-size:23px;line-height:24px;color:var(--brown)}
.h-accent{position:absolute;left:12px;font-family:"Archivo Black",sans-serif;font-size:19px;line-height:20px;color:var(--yellow)}
.h-sub{position:absolute;left:12px;font-family:"Archivo Black",sans-serif;font-size:14px;line-height:16px;color:var(--brown)}
.label{position:absolute;left:12px;right:12px;display:flex;align-items:flex-start;gap:6px;font-size:7px;font-weight:600;line-height:7.5px;color:var(--brown)}
.label svg{flex:none}
.field{position:absolute;left:12px;right:12px;height:19px;border-radius:10px;background:var(--field);font-size:6px;color:#9a9a9a;padding-left:12px;line-height:19px}
.field .caret{position:absolute;right:14px;top:8px;width:0;height:0;border-left:3px solid transparent;border-right:3px solid transparent;border-top:3.5px solid var(--ink)}
.hint{position:absolute;left:12px;right:14px;font-size:5.6px;line-height:8px;color:var(--grey-text)}
.cta{position:absolute;left:12px;right:12px;top:391px;height:23px;border-radius:12px;background:var(--yellow);color:var(--brown);font-size:8px;font-weight:600;text-align:center;line-height:23px}
.toggle-row{position:absolute;left:12px;top:372px;display:flex;align-items:center;gap:6px;font-size:5.8px;color:var(--brown)}
.toggle{width:14px;height:8px;border-radius:4px;background:#e4e4e4;position:relative}
.toggle::after{content:"";position:absolute;left:3px;top:1px;width:6px;height:6px;border-radius:50%;background:var(--green)}
.lede{position:absolute;left:12px;right:14px;top:198px;font-size:7.2px;line-height:12px;color:var(--grey-text)}
.tile{position:absolute;top:281px;width:80px;height:108px;border-radius:24px;background:var(--yellow);text-align:center;color:var(--brown);font-size:8px;font-weight:600;line-height:9.5px}
.tile svg{display:block;margin:28px auto 10px}
.back-arrow{position:absolute;left:13px;top:33px}
.slider{position:absolute;left:12px;width:119px;height:1px;background:#d8d8d8}
.slider .fill{position:absolute;left:0;top:-0.5px;height:2px;background:var(--yellow)}
.slider .knob{position:absolute;top:-3.5px;width:8px;height:8px;border-radius:50%;background:var(--brown)}
.slider-label{position:absolute;left:12px;font-size:5.2px;color:var(--grey-text)}
.count{position:absolute;left:153px;width:30px;height:20px;border-radius:10px;background:var(--field);font-size:6px;color:var(--brown);text-align:center;line-height:20px}
.lead-bold{position:absolute;left:13px;right:12px;top:102px;font-size:7px;font-weight:700;line-height:10px;color:var(--brown)}
.lead-reg{position:absolute;left:13px;right:12px;top:124px;font-size:7px;line-height:9px;color:var(--brown)}
.bundle{position:absolute;left:13px;width:171px;border-radius:14px;background:var(--white);box-shadow:0 2px 10px rgba(0,0,0,.08);overflow:hidden}
.bundle-art{position:absolute;left:0;top:0;width:171px;height:106px}
.badge{position:absolute;left:10px;top:10px;padding:0 7px;height:11px;border-radius:6px;background:var(--yellow);color:var(--white);font-size:5.5px;font-weight:700;line-height:11px;letter-spacing:.3px}
.brewery{position:absolute;left:7px;top:114px;font-size:7.5px;font-weight:600;color:var(--brown)}
.beer-name{position:absolute;left:7px;top:124px;font-family:"Archivo Black",sans-serif;font-size:14px;color:var(--yellow)}
.abv{position:absolute;left:7px;top:142px;font-size:6.5px;font-weight:600;color:var(--brown)}
.abv span{color:var(--teal);letter-spacing:1px;margin-left:5px;font-size:6px}
.spec{position:absolute;left:7px;top:157px;width:157px;height:35px;border-radius:9px;background:#f6f6f6;display:flex;justify-content:space-around;padding-top:7px}
.spec div{font-size:7.5px;font-weight:600;color:var(--brown);line-height:10px}
.spec small{display:block;font-size:6.2px;font-weight:400;color:var(--grey-text)}
.was{position:absolute;left:7px;top:200px;font-size:6.5px;color:var(--grey-text);text-decoration:line-through}
.now{position:absolute;left:7px;top:209px;font-size:11px;font-weight:700;color:var(--brown)}
.get{position:absolute;left:90px;top:201px;width:74px;height:20px;border-radius:10px;background:var(--yellow);color:var(--brown);font-size:8px;font-weight:600;text-align:center;line-height:20px}
</style>
</head>
<body>

<header class="heading">
  <h1>KEGS APP</h1>
  <p>UI SCREENS</p>
</header>

<!-- Splash -->
<section class="screen promo row1 c1">
  <span class="time">9:41</span><span class="island"></span>
  <svg class="status-icons" width="40" height="7" viewBox="0 0 40 7"><rect x="0" y="4.5" width="1.6" height="2.5" fill="#3b2216"/><rect x="2.5" y="3" width="1.6" height="4" fill="#3b2216"/><rect x="5" y="1.5" width="1.6" height="5.5" fill="#3b2216"/><rect x="7.5" y="0" width="1.6" height="7" fill="#3b2216"/><path d="M13 2.5a6 6 0 0 1 8 0M14.5 4a3.6 3.6 0 0 1 5 0" stroke="#3b2216" stroke-width="1.1" fill="none"/><circle cx="17" cy="6" r="0.9" fill="#3b2216"/><rect x="26" y="0.5" width="11" height="6" rx="1.5" fill="#3b2216"/><rect x="37.6" y="2.3" width="1" height="2.4" fill="#3b2216"/></svg>
  <div class="art" role="img" aria-label="Faint repeating pattern of outlined beer glasses and mugs" style="left:0;top:40px;width:195px;height:384px;border-radius:0;background:linear-gradient(180deg,rgba(0,0,0,0) 0%,rgba(196,140,0,.08) 100%)"></div>
  <div class="brand-mark">BARREL<br>BAY<br>RUNNER</div>
</section>

<!-- Promo 1 -->
<section class="screen promo row1 c2">
  <span class="time">9:41</span><span class="island"></span>
  <svg class="status-icons" width="40" height="7" viewBox="0 0 40 7"><rect x="0" y="4.5" width="1.6" height="2.5" fill="#3b2216"/><rect x="2.5" y="3" width="1.6" height="4" fill="#3b2216"/><rect x="5" y="1.5" width="1.6" height="5.5" fill="#3b2216"/><rect x="7.5" y="0" width="1.6" height="7" fill="#3b2216"/><path d="M13 2.5a6 6 0 0 1 8 0M14.5 4a3.6 3.6 0 0 1 5 0" stroke="#3b2216" stroke-width="1.1" fill="none"/><circle cx="17" cy="6" r="0.9" fill="#3b2216"/><rect x="26" y="0.5" width="11" height="6" rx="1.5" fill="#3b2216"/><rect x="37.6" y="2.3" width="1" height="2.4" fill="#3b2216"/></svg>
  <div class="art" role="img" aria-label="3D cartoon of a partygoer in a party hat celebrating among confetti" style="left:40px;top:48px;width:115px;height:190px;background:radial-gradient(ellipse at 50% 45%,rgba(80,130,180,.35),rgba(247,181,0,0) 70%)"></div>
  <h2 class="promo-title" style="top:247px">THROW A BASH</h2>
  <div class="promo-body" style="top:269px">
    <p>Who loves a party? We all love a party, but we don't all love having to plan for one. Are you over the anxiety that comes with being the hostess with the mostess? Want to make sure your guests are sufficiently fed and watered? Well when it comes to beer drinkers, we got you covered!</p>
  </div>
  <div class="dots"><i class="on"></i><i></i><i></i></div>
  <span class="nav-link next">Next</span>
</section>

<!-- Promo 2 -->
<section class="screen promo row1 c3">
  <span class="time">9:41</span><span class="island"></span>
  <svg class="status-icons" width="40" height="7" viewBox="0 0 40 7"><rect x="0" y="4.5" width="1.6" height="2.5" fill="#3b2216"/><rect x="2.5" y="3" width="1.6" height="4" fill="#3b2216"/><rect x="5" y="1.5" width="1.6" height="5.5" fill="#3b2216"/><rect x="7.5" y="0" width="1.6" height="7" fill="#3b2216"/><path d="M13 2.5a6 6 0 0 1 8 0M14.5 4a3.6 3.6 0 0 1 5 0" stroke="#3b2216" stroke-width="1.1" fill="none"/><circle cx="17" cy="6" r="0.9" fill="#3b2216"/><rect x="26" y="0.5" width="11" height="6" rx="1.5" fill="#3b2216"/><rect x="37.6" y="2.3" width="1" height="2.4" fill="#3b2216"/></svg>
  <div class="art" role="img" aria-label="3D cartoon calendar with a clock" style="left:42px;top:80px;width:112px;height:102px;background:linear-gradient(160deg,#8a80ea 0%,#e3e0f4 45%,#d9d6f2 100%)"></div>
  <h2 class="promo-title single-line" style="top:228px">MORE PARTY, LESS PLANNING</h2>
  <div class="promo-body" style="top:249px">
    <p>No more last minute runs to the bottle shop, supermarket or local wholesalers.</p>
    <p>No more back breaking journeys carrying heavy beer bottles and cans across your neighbourhood.</p>
    <p>No more worries about fridge capacity and no more warm beers for your guests.</p>
  </div>
  <div class="dots"><i></i><i class="on"></i><i></i></div>
  <span class="nav-link back">Back</span><span class="nav-link next">Next</span>
</section>

<!-- Promo 3 -->
<section class="screen promo row1 c4">
  <span class="time">9:41</span><span class="island"></span>
  <svg class="status-icons" width="40" height="7" viewBox="0 0 40 7"><rect x="0" y="4.5" width="1.6" height="2.5" fill="#3b2216"/><rect x="2.5" y="3" width="1.6" height="4" fill="#3b2216"/><rect x="5" y="1.5" width="1.6" height="5.5" fill="#3b2216"/><rect x="7.5" y="0" width="1.6" height="7" fill="#3b2216"/><path d="M13 2.5a6 6 0 0 1 8 0M14.5 4a3.6 3.6 0 0 1 5 0" stroke="#3b2216" stroke-width="1.1" fill="none"/><circle cx="17" cy="6" r="0.9" fill="#3b2216"/><rect x="26" y="0.5" width="11" height="6" rx="1.5" fill="#3b2216"/><rect x="37.6" y="2.3" width="1" height="2.4" fill="#3b2216"/></svg>
  <div class="art" role="img" aria-label="3D cartoon hand holding a gold coin" style="left:54px;top:50px;width:76px;height:135px;background:linear-gradient(180deg,#f4c49a 0%,#eab48a 70%,#7fa0e6 100%)"></div>
  <h2 class="promo-title" style="top:202px">SAVE MONEY AND THE<br>PLANET</h2>
  <div class="promo-body" style="top:238px">
    <p>Finally a <b>cost efficient, environmentally sustainable, no hassle</b> and <b>fun</b> way to keep all the beer drinkers at your party smiling.</p>
    <p>Our service enables you to throw a keg party of your dreams by removing the logistical challenges so you and your guests can focus on having a good time.</p>
    <p>Never worry about your beer supply again.</p>
  </div>
  <div class="dots"><i></i><i></i><i class="on"></i></div>
  <span class="nav-link back">Back</span><span class="nav-link next">Next</span>
</section>

<!-- Before we begin -->
<section class="screen row2 c1">
  <span class="time">9:41</span><span class="island"></span>
  <svg class="status-icons" width="40" height="7" viewBox="0 0 40 7"><rect x="0" y="4.5" width="1.6" height="2.5" fill="#3b2216"/><rect x="2.5" y="3" width="1.6" height="4" fill="#3b2216"/><rect x="5" y="1.5" width="1.6" height="5.5" fill="#3b2216"/><rect x="7.5" y="0" width="1.6" height="7" fill="#3b2216"/><path d="M13 2.5a6 6 0 0 1 8 0M14.5 4a3.6 3.6 0 0 1 5 0" stroke="#3b2216" stroke-width="1.1" fill="none"/><circle cx="17" cy="6" r="0.9" fill="#3b2216"/><rect x="26" y="0.5" width="11" height="6" rx="1.5" fill="#3b2216"/><rect x="37.6" y="2.3" width="1" height="2.4" fill="#3b2216"/></svg>
  <div class="art" role="img" aria-label="Scattered illustrated tilted beer mugs and glasses" style="left:56px;top:34px;width:139px;height:142px;border-radius:14px 0 0 14px;background:linear-gradient(135deg,var(--yellow-soft) 0%,rgba(253,231,166,.35) 100%)"></div>
  <h2 class="h-accent" style="top:152px">BEFORE</h2>
  <h3 class="h-sub" style="top:172px">WE BEGIN...</h3>
  <div class="label" style="top:213px"><svg width="10" height="10" viewBox="0 0 10 10"><rect width="10" height="10" rx="2" fill="#f7b500"/><path d="M3 3l4 4M7 3L3 7" stroke="#fff" stroke-width="1.2"/></svg><span>We need to check if we deliver in your area</span></div>
  <div class="field" style="top:232px">Address lookup</div>
  <div class="hint" style="top:256px">We only deliver in selected London boroughs during the pilot.</div>
  <div class="label" style="top:290px"><svg width="10" height="11" viewBox="0 0 10 11"><path d="M5 0l5 2v3.5C10 8.5 7.5 10.3 5 11 2.5 10.3 0 8.5 0 5.5V2z" fill="#f7b500"/><rect x="4.3" y="3" width="1.4" height="3.5" fill="#fff"/><circle cx="5" cy="8" r=".8" fill="#fff"/></svg><span style="padding-top:2px">Making sure you are grown up</span></div>
  <div class="field" style="top:307px">DD/MM/YYYY</div>
  <div class="toggle-row"><span class="toggle"></span><span>Yes, i am over 18 years old to use this service.</span></div>
  <div class="cta">Let the party begin</div>
</section>

<!-- Let's start -->
<section class="screen row2 c2">
  <span class="time">9:41</span><span class="island"></span>
  <svg class="status-icons" width="40" height="7" viewBox="0 0 40 7"><rect x="0" y="4.5" width="1.6" height="2.5" fill="#3b2216"/><rect x="2.5" y="3" width="1.6" height="4" fill="#3b2216"/><rect x="5" y="1.5" width="1.6" height="5.5" fill="#3b2216"/><rect x="7.5" y="0" width="1.6" height="7" fill="#3b2216"/><path d="M13 2.5a6 6 0 0 1 8 0M14.5 4a3.6 3.6 0 0 1 5 0" stroke="#3b2216" stroke-width="1.1" fill="none"/><circle cx="17" cy="6" r="0.9" fill="#3b2216"/><rect x="26" y="0.5" width="11" height="6" rx="1.5" fill="#3b2216"/><rect x="37.6" y="2.3" width="1" height="2.4" fill="#3b2216"/></svg>
  <div class="art" role="img" aria-label="Scattered illustrated tilted beer mugs and glasses" style="left:56px;top:34px;width:139px;height:142px;border-radius:14px 0 0 14px;background:linear-gradient(135deg,var(--yellow-soft) 0%,rgba(253,231,166,.35) 100%)"></div>
  <h2 class="h-accent" style="top:152px">LET’S</h2>
  <h3 class="h-sub" style="top:172px">START...</h3>
  <p class="lede">Lorem ipsum dolor sit amet, consectetur adipiscing elit. Nulla et diam nulla. Suspendisse aliquam gravida leo, sit amet mollis sapien. In elementum purus nec neque sodales, ac volutpat diam egestas.</p>
  <div class="tile" style="left:12px"><svg width="22" height="20" viewBox="0 0 22 20"><rect x="2" y="6" width="18" height="13" rx="3" fill="#fff"/><rect x="0" y="4" width="22" height="4" rx="2" fill="#fde7a6"/><path d="M6 4l3-4M16 4l-3-4" stroke="#fff" stroke-width="1.5"/><rect x="8" y="11" width="1.6" height="4" fill="#f7b500"/><rect x="12" y="11" width="1.6" height="4" fill="#f7b500"/></svg>Pick your<br>Kegs</div>
  <div class="tile" style="left:103px"><svg width="20" height="22" viewBox="0 0 20 22"><rect x="0" y="3" width="20" height="19" rx="4" fill="#fff"/><rect x="0" y="3" width="20" height="6" rx="3" fill="#fde7a6"/><rect x="5" y="0" width="2" height="6" rx="1" fill="#fff"/><rect x="13" y="0" width="2" height="6" rx="1" fill="#fff"/><circle cx="6" cy="14" r="1.3" fill="#f7b500"/><circle cx="10" cy="14" r="1.3" fill="#f7b500"/><circle cx="6" cy="18" r="1.3" fill="#f7b500"/></svg>Plan your<br>Party</div>
</section>

<!-- Tell us about your party -->
<section class="screen row2 c3">
  <span class="time">9:41</span><span class="island"></span>
  <svg class="status-icons" width="40" height="7" viewBox="0 0 40 7"><rect x="0" y="4.5" width="1.6" height="2.5" fill="#3b2216"/><rect x="2.5" y="3" width="1.6" height="4" fill="#3b2216"/><rect x="5" y="1.5" width="1.6" height="5.5" fill="#3b2216"/><rect x="7.5" y="0" width="1.6" height="7" fill="#3b2216"/><path d="M13 2.5a6 6 0 0 1 8 0M14.5 4a3.6 3.6 0 0 1 5 0" stroke="#3b2216" stroke-width="1.1" fill="none"/><circle cx="17" cy="6" r="0.9" fill="#3b2216"/><rect x="26" y="0.5" width="11" height="6" rx="1.5" fill="#3b2216"/><rect x="37.6" y="2.3" width="1" height="2.4" fill="#3b2216"/></svg>
  <svg class="back-arrow" width="13" height="9" viewBox="0 0 13 9"><path d="M12.5 4.5H1M5 .7L1 4.5 5 8.3" stroke="#3b2216" stroke-width="1.2" fill="none"/></svg>
  <h2 class="h-accent" style="top:56px">TELL US ABOUT</h2>
  <h3 class="h-sub" style="top:77px">YOUR PARTY...</h3>
  <div class="label" style="top:121px"><svg width="9" height="9" viewBox="0 0 9 9"><rect y="1" width="9" height="8" rx="1.5" fill="#f7b500"/><rect x="2" y="0" width="1.2" height="2.5" fill="#f7b500"/><rect x="5.8" y="0" width="1.2" height="2.5" fill="#f7b500"/><rect x="1.5" y="4" width="6" height="1" fill="#fff"/></svg><span style="padding-top:1px">When is your party?</span></div>
  <div class="field" style="top:137px">DD/MM/YYYY</div>
  <div class="hint" style="top:160px">We will pick up the empty keg the next day</div>
  <div class="label" style="top:185px"><svg width="9" height="10" viewBox="0 0 9 10"><rect width="9" height="8.5" rx="2" fill="#f7b500"/><path d="M3 8.5L4.5 10 6 8.5" fill="#f7b500"/><circle cx="4.5" cy="3.3" r="1.3" fill="#fff"/><path d="M2.3 7a2.2 2.2 0 0 1 4.4 0z" fill="#fff"/></svg><span style="padding-top:1px">Tell us about the people attending</span></div>
  <div class="slider" style="top:205px"><span class="fill" style="width:56px"></span><span class="knob" style="left:52px"></span></div>
  <div class="slider-label" style="top:214px">Booze hound (good for 8 pints)</div>
  <div class="count" style="top:199px">08</div>
  <div class="slider" style="top:231px"><span class="fill" style="width:23px"></span><span class="knob" style="left:19px"></span></div>
  <div class="slider-label" style="top:240px">Thirsty but thoughtful (good for 5 pints)</div>
  <div class="count" style="top:225px">03</div>
  <div class="slider" style="top:257px"><span class="fill" style="width:46px"></span><span class="knob" style="left:42px"></span></div>
  <div class="slider-label" style="top:266px">Country club bore (good for 2 pints)</div>
  <div class="count" style="top:251px">07</div>
  <div class="label" style="top:291px"><svg width="9" height="10" viewBox="0 0 9 10"><path d="M0 0h9v6.5L4.5 10 0 6.5z" fill="#f7b500"/><rect x="2" y="2.5" width="5" height="2.5" rx="1" fill="#fff"/></svg><span style="padding-top:1px">What kind of beer do you like?</span></div>
  <div class="field" style="top:307px">Select your beer<span class="caret"></span></div>
  <div class="label" style="top:344px"><svg width="10" height="9" viewBox="0 0 10 9"><rect x="0" y="3.5" width="2.3" height="5.5" fill="#f7b500"/><path d="M3 3.5L5.5 0c1 0 1.5.8 1.2 1.8L6.2 3.5H9.2c.6 0 .9.6.7 1.1L8.5 8.5c-.2.3-.5.5-.8.5H3z" fill="#f7b500"/></svg><span style="padding-top:1px">What kind of glassware do you require?</span></div>
  <div class="field" style="top:360px">Select your glass<span class="caret"></span></div>
  <div class="cta">Get recommendation</div>
</section>

<!-- Recommendation -->
<section class="screen row2 c4">
  <span class="time">9:41</span><span class="island"></span>
  <svg class="status-icons" width="40" height="7" viewBox="0 0 40 7"><rect x="0" y="4.5" width="1.6" height="2.5" fill="#3b2216"/><rect x="2.5" y="3" width="1.6" height="4" fill="#3b2216"/><rect x="5" y="1.5" width="1.6" height="5.5" fill="#3b2216"/><rect x="7.5" y="0" width="1.6" height="7" fill="#3b2216"/><path d="M13 2.5a6 6 0 0 1 8 0M14.5 4a3.6 3.6 0 0 1 5 0" stroke="#3b2216" stroke-width="1.1" fill="none"/><circle cx="17" cy="6" r="0.9" fill="#3b2216"/><rect x="26" y="0.5" width="11" height="6" rx="1.5" fill="#3b2216"/><rect x="37.6" y="2.3" width="1" height="2.4" fill="#3b2216"/></svg>
  <svg class="back-arrow" width="13" height="9" viewBox="0 0 13 9"><path d="M12.5 4.5H1M5 .7L1 4.5 5 8.3" stroke="#3b2216" stroke-width="1.2" fill="none"/></svg>
  <h2 class="h-accent" style="top:56px">HERE IS</h2>
  <h3 class="h-sub" style="top:77px">WHAT WE THINK...</h3>
  <p class="lead-bold">Based on what you told us we think you need at least 72 pints.</p>
  <p class="lead-reg">These bundles should make your party awesome.</p>
  <article class="bundle" style="top:154px;height:229px">
    <div class="bundle-art" role="img" aria-label="Blue keg product artwork for a session IPA" style="background:linear-gradient(135deg,#3da3f0 0%,#2f8fe0 55%,#1f5fb0 100%)"></div>
    <span class="badge">FEATURED</span>
    <div class="brewery">Tallowmere Brewery</div>
    <div class="beer-name">Session IPA</div>
    <div class="abv">5.2% Vol<span>★★★★★</span></div>
    <div class="spec">
      <div>35l Keg<small>x 2</small></div>
      <div>Plastic cups<small>x 40</small></div>
      <div>Tap<small>Simple</small></div>
    </div>
    <div class="was">$210.50</div>
    <div class="now">$110.50</div>
    <div class="get">Get</div>
  </article>
  <article class="bundle" style="top:396px;height:40px">
    <div class="bundle-art" role="img" aria-label="Orange keg product artwork" style="background:linear-gradient(135deg,#ec8a2c 0%,var(--orange) 100%)"></div>
    <span class="badge">FEATURED</span>
  </article>
</section>

</body>
</html>
```